History Wall for Corporate Office

We are working on our corporate office wall to include a graphic with our history, and when we opened the schools and dance studios.
We are looking for a professional look, vibrant graphic, but clean and very clear to understand.
The wall is going up from floor 1 to floor 2. Please see photos attached as reference.
Measurements provided as well.
Do not include the master logo as part of this design, as the master logo it's placed in the wall right next to this one (photo as reference will show this).
Things to consider:
- We want to include photos of the schools/studio openings. Attached are the photos of each school opening.
- Follow brand guidelines
- Mainly using Master Color palette (blues and yellows) with touches of the other colors if needed
Here's the order of school/studio openings:
1968 Bright Path Hollowmere
1971 Bright Path Fernwick
1975 Bright Path Harlow
1976 The Bright Path Conservatory of Dance
1978 Bright Path Collegiate
1979 Bright Path Cobalt • Preschool & Elementary School
1980 Bright Path Las Brisas
1981 Bright Path Cedar Crest
1984 Bright Path Middle School
1989 Bright Path Dorsey
1990 Bright Path Whitford
2005 Bright Path Garnet
2008 Bright Path Schools 40th Anniversary
2015 NHMS Talbot Studio
2016 NHMS Aspen Hollow Studio
2017 NHMS Cedar Crest Studio
2018 Bright Path Schools 50th Anniversary
2021 Kinetic Leagues Coastline
2022 NHMS Cedar Crest Studio
2024 Bright Path Sutter Ridge
Fonts to be used: Fellix (main font) and Handsome (highlights-if needed)
Sending two graphic ideas as reference of the design direction we would like to have.

```html
<!DOCTYPE html>
<html lang="en">
<head>
<meta charset="utf-8">
<title>Bright Path History Wall</title>
<link rel="stylesheet" href="https://fonts.googleapis.com/css2?family=Figtree:wght@400;500;600&family=Caveat:wght@500;600&display=swap">
<style>
  :root {
    --wall: #ffffff;
    --frame: #d6d6d6;
    --sky: #62b8f8;
    --bubble: #b7d9f7;
    --star-pale: #e7f0f8;
    --star-line: #78abd9;
    --star-deep: #3f86e8;
    --star-mid: #5aa8f0;
    --route: #f5b400;
    --accent-orange: #f7931e;
    --accent-amber: #fbb03b;
    --bulb-yellow: #f9d63a;
    --bulb-gold: #f2c21b;
    --ink: #1b1b1b;
    --year: #3a78de;
    --photo-top: #93b7da;
    --photo-bottom: #5f7350;
  }
  html, body {
    margin: 0;
    padding: 0;
    width: 933px;
    height: 1200px;
    overflow: hidden;
    background: var(--wall);
  }
  .history-wall {
    display: block;
    width: 933px;
    height: 1200px;
  }
  .milestone-year {
    font-family: "Caveat", cursive;
    font-weight: 500;
    font-size: 34px;
    fill: var(--year);
  }
  .milestone-name {
    font-family: "Figtree", sans-serif;
    font-weight: 500;
    font-size: 19.5px;
    fill: var(--ink);
  }
  .opening-photo { fill: url(#photo-tone); }
  .wall-frame { fill: none; stroke: var(--frame); stroke-width: 1.5; }
  .journey-route {
    fill: none;
    stroke: var(--route);
    stroke-width: 5;
    stroke-dasharray: 18 12;
    stroke-linecap: round;
  }
  .deco-bubble { fill: var(--bubble); }
  .illustration-bulb { fill: url(#bulb-tone); }
  .illustration-rocket { fill: url(#rocket-tone); }
  .music-badge { fill: url(#badge-tone); }
</style>
</head>
<body>
<svg class="history-wall" viewBox="0 0 1710 2200" preserveAspectRatio="none" xmlns="http://www.w3.org/2000/svg">
  <defs>
    <linearGradient id="photo-tone" x1="0" y1="0" x2="0" y2="1">
      <stop offset="0" stop-color="var(--photo-top)"/>
      <stop offset="0.6" stop-color="#9a9a86"/>
      <stop offset="1" stop-color="var(--photo-bottom)"/>
    </linearGradient>
    <linearGradient id="bulb-tone" x1="0" y1="0" x2="0" y2="1">
      <stop offset="0" stop-color="var(--bulb-yellow)"/>
      <stop offset="1" stop-color="var(--bulb-gold)"/>
    </linearGradient>
    <linearGradient id="rocket-tone" x1="0" y1="0" x2="1" y2="0">
      <stop offset="0" stop-color="var(--bulb-gold)"/>
      <stop offset="1" stop-color="var(--bulb-yellow)"/>
    </linearGradient>
    <linearGradient id="badge-tone" x1="0" y1="0" x2="1" y2="1">
      <stop offset="0" stop-color="var(--accent-orange)"/>
      <stop offset="1" stop-color="var(--accent-amber)"/>
    </linearGradient>
    <polygon id="star-shape" stroke-linejoin="round" points="0,-1 0.294,-0.405 0.951,-0.309 0.476,0.155 0.588,0.809 0,0.5 -0.588,0.809 -0.476,0.155 -0.951,-0.309 -0.294,-0.405"/>
  </defs>

  <rect class="wall-frame" x="110" y="105" width="1480" height="1965"/>

  <!-- main sky shape -->
  <path fill="var(--sky)" d="M120 1190 C120 1100 250 1070 380 1030 C500 990 560 900 580 700 C600 520 650 460 720 460 C790 460 820 520 860 560 L1040 740 C1080 780 1150 775 1230 770 L1450 740 C1540 730 1590 780 1565 860 C1540 960 1420 1150 1380 1230 C1360 1280 1400 1320 1420 1350 L1420 1700 L1300 1700 L900 1830 C800 1900 720 1940 640 1935 C560 1930 530 1880 530 1800 C530 1600 520 1520 480 1470 C430 1400 320 1350 240 1300 C170 1260 120 1240 120 1190 Z"/>

  <!-- stairway edge of the wall -->
  <polygon fill="var(--wall)" points="1600,1268 1505,1268 1505,1347 1410,1347 1410,1428 1313,1428 1313,1510 1213,1510 1213,1590 1117,1590 1117,1668 1022,1668 1022,1750 930,1750 930,1830 833,1830 833,1910 738,1910 738,1990 641,1990 641,2070 1600,2070"/>
  <polyline fill="none" stroke="var(--frame)" stroke-width="1.5" points="1600,1268 1505,1268 1505,1347 1410,1347 1410,1428 1313,1428 1313,1510 1213,1510 1213,1590 1117,1590 1117,1668 1022,1668 1022,1750 930,1750 930,1830 833,1830 833,1910 738,1910 738,1990 641,1990 641,2070"/>

  <!-- big pale star -->
  <use href="#star-shape" fill="#ffffff" stroke="#ffffff" stroke-width="0.08" transform="translate(905 478) scale(222)"/>
  <use href="#star-shape" fill="var(--star-pale)" stroke="var(--star-line)" stroke-width="0.012" transform="translate(915 470) scale(222)"/>

  <!-- start and finish bubbles -->
  <circle class="deco-bubble" cx="257" cy="830" r="62"/>
  <circle class="deco-bubble" cx="1062" cy="310" r="62"/>
  <use href="#star-shape" fill="#ffffff" transform="translate(282 822) scale(22)"/>
  <use href="#star-shape" fill="var(--star-mid)" transform="translate(322 826) scale(22)"/>
  <use href="#star-shape" fill="var(--star-mid)" transform="translate(319 779) scale(13)"/>
  <use href="#star-shape" fill="#ffffff" transform="translate(1085 302) scale(22)"/>
  <use href="#star-shape" fill="var(--star-mid)" transform="translate(1126 305) scale(22)"/>
  <use href="#star-shape" fill="var(--star-mid)" transform="translate(1124 258) scale(13)"/>

  <!-- journey route -->
  <path class="journey-route" d="M270 855 C370 845 450 900 440 980 C430 1080 350 1150 352 1250 C354 1360 380 1480 470 1505 C560 1525 640 1480 650 1400 C660 1280 630 1160 660 1070 C700 960 800 880 900 830 C980 795 1060 785 1130 805 C1210 830 1240 910 1260 990 C1290 1070 1340 1110 1420 1105 C1520 1095 1570 1010 1565 910 C1560 830 1530 770 1480 730 C1420 680 1330 630 1220 605 C1120 585 1030 590 995 520 C960 450 975 380 1035 290"/>

  <!-- illustration areas -->
  <rect class="illustration-bulb" x="200" y="706" width="70" height="94" rx="28" role="img" aria-label="Yellow light bulb illustration marking the start of the journey"/>
  <rect class="illustration-rocket" x="1010" y="228" width="130" height="42" rx="21" transform="rotate(-33 1075 249)" role="img" aria-label="Yellow rocket illustration launching toward the future"/>
  <ellipse class="music-badge" cx="886" cy="840" rx="31" ry="26" role="img" aria-label="Orange badge with a music note and treble clef"/>
  <ellipse class="music-badge" cx="1494" cy="764" rx="31" ry="24" role="img" aria-label="Orange badge with a music note and treble clef"/>

  <!-- accent stars -->
  <use href="#star-shape" fill="var(--star-deep)" stroke="var(--star-deep)" stroke-width="0.12" transform="translate(1025 1240) scale(58)"/>
  <use href="#star-shape" fill="#ffffff" stroke="#ffffff" stroke-width="0.15" transform="translate(1115 1305) scale(29)"/>

  <!-- milestones -->
  <g class="milestone">
    <rect class="opening-photo" x="228" y="973" width="133" height="133" role="img" aria-label="Photo of the Hollowmere school opening"/>
    <text class="milestone-year" x="225" y="920">1968</text>
    <text class="milestone-name" x="226" y="943">Bright Path</text>
    <text class="milestone-name" x="226" y="964">Hollowmere</text>
  </g>
  <g class="milestone">
    <rect class="opening-photo" x="190" y="1202" width="133" height="133" role="img" aria-label="Photo of the Fernwick school opening"/>
    <text class="milestone-year" x="188" y="1150">1971</text>
    <text class="milestone-name" x="189" y="1172">Bright Path</text>
    <text class="milestone-name" x="189" y="1193">Fernwick</text>
  </g>
  <g class="milestone">
    <rect class="opening-photo" x="386" y="1238" width="133" height="133" role="img" aria-label="Photo of the Harlow school opening"/>
    <text class="milestone-year" x="385" y="1188">1975</text>
    <text class="milestone-name" x="386" y="1210">Bright Path</text>
    <text class="milestone-name" x="386" y="1231">Harlow</text>
  </g>
  <g class="milestone">
    <rect class="opening-photo" x="190" y="1430" width="133" height="133" role="img" aria-label="Photo of the Conservatory of Dance opening"/>
    <text class="milestone-year" x="188" y="1378">1976</text>
    <text class="milestone-name" x="189" y="1400">The Bright Path</text>
    <text class="milestone-name" x="189" y="1421">Conservatory of Dance</text>
  </g>
  <g class="milestone">
    <rect class="opening-photo" x="359" y="1534" width="133" height="133" role="img" aria-label="Photo of the Collegiate school opening"/>
    <text class="milestone-year" x="358" y="1698">1978</text>
    <text class="milestone-name" x="359" y="1720">Bright Path</text>
    <text class="milestone-name" x="359" y="1741">Collegiate</text>
  </g>
  <g class="milestone">
    <rect class="opening-photo" x="530" y="1534" width="133" height="133" role="img" aria-label="Photo of the Cobalt school opening"/>
    <text class="milestone-year" x="529" y="1700">1979</text>
    <text class="milestone-name" x="531" y="1720">Bright Path Cobalt</text>
    <text class="milestone-name" x="531" y="1741">Preschool &amp;</text>
    <text class="milestone-name" x="531" y="1762">Elementary School</text>
  </g>
  <g class="milestone">
    <rect class="opening-photo" x="688" y="1495" width="133" height="133" role="img" aria-label="Photo of the Las Brisas school opening"/>
    <text class="milestone-year" x="831" y="1565">1980</text>
    <text class="milestone-name" x="833" y="1587">Bright Path</text>
    <text class="milestone-name" x="833" y="1608">Las Brisas</text>
  </g>
  <g class="milestone">
    <rect class="opening-photo" x="688" y="1341" width="133" height="133" role="img" aria-label="Photo of the Cedar Crest school opening"/>
    <text class="milestone-year" x="831" y="1412">1981</text>
    <text class="milestone-name" x="833" y="1433">Bright Path</text>
    <text class="milestone-name" x="833" y="1454">Cedar Crest</text>
  </g>
  <g class="milestone">
    <rect class="opening-photo" x="688" y="1187" width="133" height="133" role="img" aria-label="Photo of the middle school opening"/>
    <text class="milestone-year" x="831" y="1260">1984</text>
    <text class="milestone-name" x="833" y="1281">Bright Path</text>
    <text class="milestone-name" x="833" y="1302">Middle School</text>
  </g>
  <g class="milestone">
    <rect class="opening-photo" x="688" y="1032" width="133" height="133" role="img" aria-label="Photo of the Dorsey school opening"/>
    <text class="milestone-year" x="831" y="1107">1989</text>
    <text class="milestone-name" x="833" y="1128">Bright Path</text>
    <text class="milestone-name" x="833" y="1149">Dorsey</text>
  </g>
  <g class="milestone">
    <rect class="opening-photo" x="593" y="815" width="133" height="133" role="img" aria-label="Photo of the Whitford school sign"/>
    <text class="milestone-year" x="590" y="765">1990</text>
    <text class="milestone-name" x="592" y="787">Bright Path</text>
    <text class="milestone-name" x="592" y="808">Whitford</text>
  </g>
  <g class="milestone">
    <rect class="opening-photo" x="899" y="943" width="133" height="133" role="img" aria-label="Photo of the Garnet school sign"/>
    <text class="milestone-year" x="894" y="915">2005</text>
    <text class="milestone-name" x="896" y="937">Bright Path Garnet</text>
  </g>
  <g class="milestone">
    <text class="milestone-year" x="833" y="757">2008</text>
    <text class="milestone-name" x="835" y="781">Bright Path Schools</text>
    <text class="milestone-name" x="835" y="802">40th Anniversary</text>
  </g>
  <g class="milestone">
    <rect class="opening-photo" x="1096" y="928" width="133" height="133" role="img" aria-label="Photo of the Talbot studio storefront"/>
    <text class="milestone-year" x="1092" y="873">2015</text>
    <text class="milestone-name" x="1095" y="895">NHMS</text>
    <text class="milestone-name" x="1095" y="919">Talbot Studio</text>
  </g>
  <g class="milestone">
    <rect class="opening-photo" x="1201" y="1102" width="133" height="133" role="img" aria-label="Photo of the Aspen Hollow studio street front"/>
    <text class="milestone-year" x="1092" y="1120">2016</text>
    <text class="milestone-name" x="1095" y="1145">NHMS</text>
    <text class="milestone-name" x="1095" y="1169">Aspen</text>
    <text class="milestone-name" x="1095" y="1193">Hollow</text>
    <text class="milestone-name" x="1095" y="1217">Studio</text>
  </g>
  <g class="milestone">
    <rect class="opening-photo" x="1343" y="941" width="133" height="133" role="img" aria-label="Photo of the Cedar Crest studio storefront"/>
    <text class="milestone-year" x="1338" y="888">2017</text>
    <text class="milestone-name" x="1341" y="910">NHMS</text>
    <text class="milestone-name" x="1341" y="934">Cedar Crest Studio</text>
  </g>
  <g class="milestone">
    <text class="milestone-year" x="1354" y="765">2018</text>
    <text class="milestone-name" x="1356" y="789">Bright Path</text>
    <text class="milestone-name" x="1356" y="810">Schools</text>
    <text class="milestone-name" x="1356" y="831">50th Anniversary</text>
  </g>
  <g class="milestone">
    <rect class="opening-photo" x="1371" y="517" width="133" height="133" role="img" aria-label="Photo of the Kinetic Leagues Coastline site"/>
    <text class="milestone-year" x="1367" y="464">2021</text>
    <text class="milestone-name" x="1370" y="487">Kinetic Leagues</text>
    <text class="milestone-name" x="1370" y="508">Coastline</text>
  </g>
  <g class="milestone">
    <rect class="opening-photo" x="1157" y="640" width="133" height="130" role="img" aria-label="Photo of the Cedar Crest studio storefront"/>
    <text class="milestone-year" x="1009" y="666">2022</text>
    <text class="milestone-name" x="1012" y="689">NHMS Cedar</text>
    <text class="milestone-name" x="1012" y="713">Crest Studio</text>
  </g>
  <g class="milestone">
    <rect class="opening-photo" x="1125" y="450" width="133" height="133" role="img" aria-label="Photo of the Sutter Ridge school opening"/>
    <text class="milestone-year" x="1119" y="393">2024</text>
    <text class="milestone-name" x="1122" y="416">Bright Path</text>
    <text class="milestone-name" x="1122" y="437">Sutter Ridge</text>
  </g>
</svg>
</body>
</html>
```